Northway Trade Partners Needs a FRESH website

We would like a creative minded designer to take on the task to Re-design our website. Its a simple 5-7 pages. With no cart, no complex html. Just plain information about our company and products we import and export. Pictures added to the product section. Since Our logo its Blue, we would like the designer to use complementing colors in order to make the website look cleaner and modern.

Target Market(s)

The target audience will be companies looking to purchase plastic related products. Companies looking to purchase large quantities of plastic containers (Shampoo bottles, caps, sprayers, mist sprayers, cosmetic containers etc).

Industry/Entity Type

It Company

Font styles to use
Sans Serif

Requirements
Must have
• We have a section in which we would like to add pictures of some of the products we carry, therefore having an easy and clean way to navigate through the pictures will be a plus.

```html
<!DOCTYPE html>
<html lang="en">
<head>
<meta charset="utf-8">
<title>Northway Trade Partners</title>
<link rel="stylesheet" href="https://fonts.googleapis.com/css2?family=Open+Sans:wght@400;600&display=swap">
<style>
  :root {
    --brand-blue: #1a7fd4;
    --logo-blue: #1590e0;
    --text-dark: #333333;
    --text-body: #666666;
    --rule: #dddddd;
    --card-grey: #ececec;
    --card-shadow: #c9c9c9;
    --footer-bg: #f4f4f4;
    --bar-bg: #4a4a4a;
    --social-1: #3b5a9a;
    --social-2: #2fa9e0;
    --social-3: #f08a24;
  }
  * { box-sizing: border-box; margin: 0; padding: 0; }
  html, body { width: 1200px; height: 2181px; overflow: hidden; }
  body { position: relative; background: #fff; font-family: "Open Sans", sans-serif; color: var(--text-dark); }
  .abs { position: absolute; }

  /* Header */
  .site-header { position: absolute; left: 0; top: 0; width: 1200px; height: 132px; background: #fff; z-index: 2; }
  .brand { position: absolute; left: 87px; top: 0; width: 179px; height: 158px; background: var(--logo-blue); border: 4px solid #fff; box-shadow: 0 2px 6px rgba(0,0,0,.25); display: flex; align-items: flex-end; justify-content: center; padding: 0 10px 26px; }
  .brand-name { color: #fff; font-weight: 600; font-size: 20px; line-height: 1.2; text-align: center; }
  .main-nav { position: absolute; left: 376px; top: 64px; display: flex; }
  .main-nav a { font-size: 17px; color: var(--text-dark); text-decoration: none; padding: 0 22px; line-height: 28px; border-left: 1px solid var(--rule); }
  .main-nav a:first-child { border-left: none; color: var(--brand-blue); }
  .social { position: absolute; display: flex; gap: 10px; }
  .social span { width: 34px; height: 34px; border-radius: 50%; display: block; }
  .social .s1 { background: var(--social-1); }
  .social .s2 { background: var(--social-2); }
  .social .s3 { background: var(--social-3); }
  .social-top { left: 991px; top: 59px; }

  /* Hero */
  .hero { position: absolute; left: 0; top: 132px; width: 1200px; height: 517px; background: radial-gradient(ellipse at 65% 45%, #49d640 0%, #22b322 45%, #0d8a18 100%); }
  .hero-caption { position: absolute; left: 87px; top: 394px; width: 519px; height: 72px; background: rgba(40,60,40,.45); color: #fff; font-size: 29px; line-height: 72px; padding-left: 26px; }
  .hero-arrow { position: absolute; top: 210px; }

  /* Intro */
  .section-title { position: absolute; font-size: 30px; font-weight: 400; color: var(--brand-blue); }
  .welcome-photo { position: absolute; left: 87px; top: 760px; width: 236px; height: 239px; background: linear-gradient(135deg, #d8463a, #b72a26 60%, #7d3a55); }
  .welcome-text { position: absolute; left: 357px; top: 756px; width: 320px; font-size: 14px; line-height: 25px; color: var(--text-body); }
  .welcome-text p + p { margin-top: 6px; }
  .news-item { position: absolute; left: 780px; width: 340px; height: 70px; }
  .news-thumb { position: absolute; left: 0; top: 0; width: 99px; height: 69px; }
  .news-title { position: absolute; left: 117px; top: 0; font-size: 14px; font-weight: 600; color: var(--brand-blue); white-space: nowrap; }
  .news-text { position: absolute; left: 117px; top: 24px; width: 224px; font-size: 13px; line-height: 24px; color: var(--text-dark); }

  /* Products */
  .product-card { position: absolute; width: 319px; height: 297px; background: var(--card-grey); border-bottom: 4px solid var(--card-shadow); }
  .product-card.is-active { border-bottom-color: var(--brand-blue); }
  .product-photo { height: 197px; }
  .product-name { text-align: center; margin-top: 28px; font-size: 20px; font-weight: 400; color: var(--brand-blue); }
  .product-sub { text-align: center; margin-top: 3px; font-size: 14px; color: var(--text-body); }

  /* Footer */
  .site-footer { position: absolute; left: 0; top: 1864px; width: 1200px; height: 248px; background: var(--footer-bg); }
  .footer-col { position: absolute; top: 48px; }
  .footer-col h3 { font-size: 22px; font-weight: 400; color: var(--text-dark); margin-bottom: 20px; }
  .footer-list { list-style: none; }
  .footer-list li { font-size: 14px; color: var(--text-dark); line-height: 34px; padding-left: 20px; position: relative; }
  .footer-list li::before { content: ""; position: absolute; left: 2px; top: 15px; width: 6px; height: 6px; border-radius: 50%; background: #888; }
  .contact-row { display: flex; align-items: flex-start; gap: 16px; font-size: 14px; line-height: 26px; margin-bottom: 10px; }
  .contact-row svg { flex: none; margin-top: 5px; }
  .follow-text { font-size: 14px; line-height: 25px; color: var(--text-body); width: 300px; }
  .copyright-bar { position: absolute; left: 0; top: 2112px; width: 1200px; height: 69px; background: var(--bar-bg); color: #fff; font-size: 14px; line-height: 69px; padding-left: 87px; }
</style>
</head>
<body>

<header class="site-header">
  <div class="brand"><span class="brand-name">Northway Trade Partners</span></div>
  <nav class="main-nav">
    <a href="#">HOME</a><a href="#">ABOUT US</a><a href="#">PRODUCTS</a><a href="#">MISSION</a><a href="#">CONTACT</a>
  </nav>
  <div class="social social-top"><span class="s1"></span><span class="s2"></span><span class="s3"></span></div>
</header>

<section class="hero" role="img" aria-label="Close-up of green plastic bottles with screw caps">
  <svg class="hero-arrow" style="left:88px" width="30" height="60" viewBox="0 0 30 60"><path d="M24 4 L6 30 L24 56" fill="none" stroke="rgba(0,0,0,.35)" stroke-width="6"/></svg>
  <svg class="hero-arrow" style="left:1086px" width="30" height="60" viewBox="0 0 30 60"><path d="M6 4 L24 30 L6 56" fill="none" stroke="rgba(0,0,0,.35)" stroke-width="6"/></svg>
  <div class="hero-caption">CLARITAS EST ETIAM PROCESSUS</div>
</section>

<h2 class="section-title" style="left:87px;top:692px">Welcome to Our Website</h2>
<div class="welcome-photo" role="img" aria-label="Hands sifting through red plastic pellets"></div>
<div class="welcome-text">
  <p>Eu tortor euismodolo. Vestibulum ant psu meiop uere cubil. Cura sed quis nibhut odiocinialor mats ed iaculis ante sed vel laciniate. Eu tortor euismo dolo. Vestibulum ant psu meop primis inicibuo.</p>
  <p>Eu tortor euismodolo. Vestibulum ant psu meiop primis inicibu orci luctus ed ultrices et posuerecu bil. Cura sed quis nibhut odiocinialor mats ed iac ulis ante sed vel laciniate. Eu tortor euismodolo. Vestibulum ant psu meiop primis inicibu orci luct us ed ultrices et posuere cubil.</p>
</div>

<h2 class="section-title" style="left:774px;top:692px">Latest News</h2>
<div class="news-item" style="top:756px">
  <div class="news-thumb" role="img" aria-label="Hands holding dark plastic granules" style="background:linear-gradient(135deg,#2a2a2a,#5a4d44)"></div>
  <div class="news-title">Duis autem vel eum iriure dolor</div>
  <div class="news-text">Brianne craves the endorphin rush fueled by fitness and uses it.</div>
</div>
<div class="news-item" style="top:845px">
  <div class="news-thumb" role="img" aria-label="Pile of mixed plastic flakes" style="background:linear-gradient(135deg,#d9b9a0,#8a6f6a,#c9c2b8)"></div>
  <div class="news-title">Duis autem vel eum iriure dolor</div>
  <div class="news-text">Brianne craves the enindorphin rush fueled by fitness and uses it.</div>
</div>
<div class="news-item" style="top:934px">
  <div class="news-thumb" role="img" aria-label="Colourful plastic granules" style="background:linear-gradient(90deg,#2e7bd0,#e07a2a,#d23b3b)"></div>
  <div class="news-title">Duis autem vel eum iriure dolor</div>
  <div class="news-text">Brianne craves the enindorphin rush fueled by fitness and uses it.</div>
</div>

<h2 class="section-title" style="left:0;width:1200px;text-align:center;top:1073px">Products</h2>

<article class="product-card is-active" style="left:87px;top:1139px">
  <div class="product-photo" role="img" aria-label="Rows of blue PET preforms" style="background:linear-gradient(135deg,#3a78c0,#6a93bd,#2a5a98)"></div>
  <h3 class="product-name">PET</h3><p class="product-sub">Lorem ipsum reprehenderit minim</p>
</article>
<article class="product-card" style="left:441px;top:1139px">
  <div class="product-photo" role="img" aria-label="Clear PET resin granules" style="background:linear-gradient(135deg,#c4ccd0,#9fa9ad,#d1d7da)"></div>
  <h3 class="product-name">PET RESIN</h3><p class="product-sub">Lorem ipsum reprehenderit minim</p>
</article>
<article class="product-card" style="left:794px;top:1139px">
  <div class="product-photo" role="img" aria-label="Stack of clear blue plastic bottles" style="background:linear-gradient(135deg,#e9f2fa,#7ab3e6,#2a6fcf)"></div>
  <h3 class="product-name">PET CONTAINERS / BOTTLES</h3><p class="product-sub">Lorem ipsum reprehenderit minim</p>
</article>
<article class="product-card" style="left:87px;top:1499px">
  <div class="product-photo" role="img" aria-label="Colourful plastic containers" style="background:linear-gradient(135deg,#f08a24,#d9d83a,#3aa0d9,#e2427a)"></div>
  <h3 class="product-name">P.E.P.P. CONTAINERS / BOTTLES</h3><p class="product-sub">Lorem ipsum reprehenderit minim</p>
</article>
<article class="product-card" style="left:441px;top:1499px">
  <div class="product-photo" role="img" aria-label="Hand using a white spray bottle against green background" style="background:linear-gradient(135deg,#1c6e20,#3aa03a,#0e4a12)"></div>
  <h3 class="product-name">SPRAYERS / ATOMIZERS / PUMPS</h3><p class="product-sub">Lorem ipsum reprehenderit minim</p>
</article>
<article class="product-card" style="left:794px;top:1499px">
  <div class="product-photo" role="img" aria-label="Metal bottle molds in greyscale" style="background:linear-gradient(135deg,#3a3a3a,#a8a8a8,#555555)"></div>
  <h3 class="product-name">MOLDS</h3><p class="product-sub">Lorem ipsum reprehenderit minim</p>
</article>

<footer class="site-footer">
  <div class="footer-col" style="left:87px">
    <h3>Site Map</h3>
    <ul class="footer-list"><li>Home</li><li>About</li><li>Programs</li><li>Contact Us</li></ul>
  </div>
  <div class="footer-col" style="left:286px">
    <h3>Links</h3>
    <ul class="footer-list"><li>Consuetudium</li><li>Praesent luptum</li><li>Duis autem veum</li><li>Nam liber tempor</li></ul>
  </div>
  <div class="footer-col" style="left:529px">
    <h3>Contact</h3>
    <div class="contact-row">
      <svg width="14" height="18" viewBox="0 0 14 18"><path d="M7 0a7 7 0 0 0-7 7c0 5 7 11 7 11s7-6 7-11a7 7 0 0 0-7-7z" fill="#333"/><circle cx="7" cy="7" r="2.5" fill="#f4f4f4"/></svg>
      <div>Unit 9, Kestrel Park<br>22 Ferris Road, SA 5190</div>
    </div>
    <div class="contact-row">
      <svg width="16" height="12" viewBox="0 0 16 12"><rect width="16" height="12" fill="#333"/><path d="M0 0 L8 7 L16 0" fill="none" stroke="#f4f4f4" stroke-width="1.5"/></svg>
      <div>hello@northwaytrade.example</div>
    </div>
    <div class="contact-row">
      <svg width="14" height="14" viewBox="0 0 14 14"><path d="M3 0 L5 4 L3.5 5.5 Q5 8.5 8.5 10.5 L10 9 L14 11 L12.5 14 Q5 13 0 2.5 Z" fill="#333"/></svg>
      <div>07 5550 1842</div>
    </div>
  </div>
  <div class="footer-col" style="left:810px">
    <h3>Follow Us</h3>
    <p class="follow-text">Follow our news and events through social networks</p>
    <div class="social" style="position:static;margin-top:20px"><span class="s1"></span><span class="s2"></span><span class="s3"></span></div>
  </div>
</footer>
<div class="copyright-bar">Copyright © 2013. All Rights Reserved</div>

</body>
</html>
```